vascular clinic webdesign (wordpress+neve theme+ elementor)

Create a nice webdesign for an existing website of a vascular surgery clinic. Vascular surgery is the medical specialty that treats arteries and veins. Content should not change. First landing page we can recreate content if needed, but internal pages should not change content. We currently use Neve theme (https://plumecraft.net/skins/orla/) in a Wordpress CMS, which is highly customizable, we prefer to keep using it, as it is standard in all our sites, and will be often upgraded. We also have Elementor Pro. Please visit current domain: lumeria.net.
Page is in portuguese. But you can do anything in English that I translate later, or you can use original domain content already in portuguese.
Selected design need to be coded in wordpress+neve+elementor

Minimum pages:
First Page/Landing page (https://lumeria.net/)
Contact page (https://lumeria.net/contato/)
Post/Article page
About us (https://lumeria.net/a-clinica/)
Posts Archive (https://lumeria.net/todos-artigos/)
The team (https://lumeria.net/sobre-nos-equipe-de-cirurgia-vascular-endovascular-ecografia-angiologia/)

Target Market(s)

mostly (70%) woman, 30 to 60 years

Industry/Entity Type

Health

Coding

Coded - Design and coding required

Number of Pages Required

5+ page

Font styles to use
Serif

Requirements
Should not have
• Will not change Wordpress for any other CMS
Prefer not to change theme Neve (https://plumecraft.net/skins/orla/)

```html
<!DOCTYPE html>
<html lang="en">
<head>
<meta charset="utf-8">
<title>Lumeria — Vascular Surgeon in São Paulo</title>
<link rel="stylesheet" href="https://fonts.googleapis.com/css2?family=Cinzel:wght@400;600&family=Lexend:wght@400;600;700&family=Lato:wght@400;700&display=swap">
<style>
:root{
  --red:#9b2a22;
  --red-dark:#7d1f19;
  --navy:#1f4e7a;
  --blue:#2b73c4;
  --green:#2aa845;
  --ink:#1d1d1d;
  --text:#555;
  --muted:#8a8a8a;
  --grey:#f2f2f3;
  --pale:#f6f7fb;
  --line:#d8d8dc;
  --white:#fff;
}
*{box-sizing:border-box;margin:0;padding:0}
html,body{width:1200px;height:4882px;overflow:hidden}
body{position:relative;background:var(--white);font-family:"Lato",sans-serif;color:var(--ink)}
.abs{position:absolute}
.serif{font-family:"Cinzel",serif}
.display{font-family:"Lexend",sans-serif}

/* header */
.site-header{left:0;top:0;width:1200px;height:77px;background:var(--white);z-index:5}
.brand{left:74px;top:20px;font-family:"Cinzel",serif;font-size:30px;color:var(--ink);letter-spacing:1px}
.nav{left:445px;top:28px;display:flex;gap:30px;font-size:15px;color:var(--ink)}
.nav .active{border-bottom:2px solid var(--navy);padding-bottom:4px}
.nav-phone{left:962px;top:20px;padding-left:18px;border-left:1px solid var(--line);height:34px;display:flex;align-items:center;gap:8px;color:var(--red);font-size:15px;font-weight:700}

/* hero */
.hero{left:0;top:77px;width:1200px;height:1013px;background:var(--grey);overflow:hidden}
.hero-photo{left:0;top:0;width:1200px;height:700px;background:linear-gradient(180deg,#e9e9e6 0%,#d8c89a 30%,#b6953e 55%,#6e5a22 100%)}
.hero-title{left:152px;top:180px;font-family:"Cinzel",serif;font-size:66px;line-height:70px;color:#111}
.hero-sub{left:154px;top:326px;font-family:"Lato",sans-serif;font-size:23px;color:#222}
.btn-pill{height:44px;border-radius:22px;display:flex;align-items:center;gap:10px;padding:0 20px 0 10px;color:var(--white);font-size:12px;line-height:14px}
.btn-pill .ico{width:30px;height:30px;border-radius:50%;border:2px solid var(--white);display:flex;align-items:center;justify-content:center}
.btn-green{background:var(--green)}
.btn-red{background:var(--red)}
.form-card{left:133px;top:548px;width:427px;height:376px;background:var(--white);border:1px solid var(--line);box-shadow:0 3px 14px rgba(0,0,0,.08);padding:34px 22px}
.form-card h2{font-family:"Cinzel",serif;font-weight:400;color:var(--red);font-size:28px;text-align:center}
.form-card p{text-align:center;font-size:12px;color:#333;margin-top:6px}
.field{border:1px solid var(--line);font-size:11px;color:#333;padding:10px 14px;height:34px}
.submit{position:absolute;right:22px;bottom:40px;background:var(--red);color:var(--white);font-size:13px;padding:10px 24px}
.hero-claim{left:634px;top:725px;font-family:"Lexend",sans-serif;font-weight:600;font-size:42px;line-height:52px;color:var(--ink)}
.hero-claim small{display:block;font-size:26px;line-height:40px;margin-top:8px}

/* specialist */
.section-title{width:1200px;left:0;text-align:center;font-family:"Lexend",sans-serif;font-weight:600;font-size:33px;line-height:44px;color:var(--ink)}
.section-title .navy{color:var(--navy)}
.section-title .red{color:var(--red)}
.feature{left:160px;width:460px;display:flex;gap:24px}
.feature .icon{flex:none;width:74px;height:74px;border-radius:50%;border:2px solid #e2e6ee;background:#f4f6fa}
.feature h3{font-size:18px;font-weight:400;color:#222;margin-bottom:12px}
.feature p{font-size:12px;line-height:19px;color:var(--text)}
.img-fill{border-radius:4px}

/* arterial */
.arterial{left:0;top:1770px;width:1200px;height:483px;background:var(--pale)}
.arterial .panel{left:0;top:0;width:335px;height:483px;background:linear-gradient(135deg,#2f7ed0,#1e5fa8)}
.play{left:298px;top:122px;width:98px;height:98px;border-radius:50%;background:var(--red-dark);display:flex;align-items:center;justify-content:center}
.play span{width:48px;height:48px;border-radius:50%;background:var(--white);display:flex;align-items:center;justify-content:center}

/* specialties */
.spec-label{font-size:17px;font-weight:700;color:#333;letter-spacing:.3px}
.orbit-dot{width:58px;height:58px;border-radius:50%;background:var(--white);border:2px solid #cfd3da}

/* testimonials */
.testimonials{left:0;top:2838px;width:1200px;height:482px;background:var(--grey)}
.t-card{top:185px;width:282px;height:205px;background:var(--white);padding:34px 36px}
.t-card p{font-size:11px;line-height:21px;color:var(--text)}
.t-person{display:flex;align-items:center;gap:12px;margin-top:18px;position:relative}
.t-person .avatar{width:40px;height:40px;border-radius:50%;background:#b8a596}
.t-person b{display:block;font-size:14px;color:#222}
.t-person small{font-size:11px;color:var(--muted)}
.t-person .quote{position:absolute;right:0;top:-4px;font-family:"Lexend",sans-serif;font-size:38px;color:#c9c9c9}
.t-card.featured{background:var(--navy)}
.t-card.featured p,.t-card.featured b,.t-card.featured small,.t-card.featured .quote{color:var(--white)}

/* banner */
.banner{left:0;top:3320px;width:1200px;height:490px;overflow:hidden;background:linear-gradient(180deg,#2c3540 0%,#4e5660 40%,#6a6448 70%,#3d3a25 100%)}
.banner h2{position:absolute;width:1200px;top:76px;text-align:center;font-family:"Lato",sans-serif;font-weight:700;font-size:25px;line-height:34px;color:var(--white)}
.banner .sub{position:absolute;width:1200px;top:162px;text-align:center;font-style:italic;font-size:17px;color:var(--white)}

/* blog */
.blog-card{top:3890px;width:275px;height:355px;background:var(--white);box-shadow:0 3px 14px rgba(0,0,0,.09)}
.blog-card .thumb{height:162px}
.blog-card .body{padding:22px 30px}
.blog-card .date{font-size:11px;color:var(--muted)}
.blog-card h3{font-size:13px;font-weight:700;color:#222;margin:12px 0 10px;letter-spacing:.3px}
.blog-card p{font-size:12px;line-height:16px;color:var(--text)}
.blog-card .more{display:block;margin-top:12px;font-size:11px;font-weight:700;color:var(--red)}
.view-all{left:530px;top:4285px;width:140px;height:40px;border-radius:20px;background:var(--red);color:var(--white);font-size:16px;display:flex;align-items:center;justify-content:center}

/* footer */
.site-footer{left:0;top:4400px;width:1200px;height:482px;background:var(--grey)}
.disclaimer{left:132px;top:126px;width:415px;font-size:9.5px;line-height:17px;color:#555}
.social{left:132px;top:274px;display:flex;gap:8px}
.social span{width:32px;height:32px;border-radius:50%;background:var(--navy)}
.f-head{font-size:17px;color:#111}
.contact-row{display:flex;align-items:center;gap:18px;font-size:13px;line-height:18px;color:#222}
.contact-row .c-ico{flex:none;width:30px;height:30px;border-radius:50%;background:#bcbcc0;display:flex;align-items:center;justify-content:center}
.info-list{list-style:none;font-size:12px;color:#222}
.info-list li{height:29px}
.info-list li::before{content:"›";margin-right:8px}
.copyright{left:132px;top:395px;font-size:13px;color:#333}
.badge{top:370px}
</style>
</head>
<body>

<header class="site-header abs">
  <div class="brand abs">Lumeria</div>
  <nav class="nav abs">
    <span class="active">About Us</span><span>The Team</span><span>Vascular Problems</span><span>Solutions</span><span>Contact</span>
  </nav>
  <div class="nav-phone abs">
    <svg width="16" height="16" viewBox="0 0 24 24" fill="none" stroke="#9b2a22" stroke-width="2"><path d="M5 3h4l2 5-3 2a12 12 0 0 0 6 6l2-3 5 2v4a2 2 0 0 1-2 2A18 18 0 0 1 3 5a2 2 0 0 1 2-2z"/></svg>
    (011) 4820-1170
  </div>
</header>

<section class="hero abs">
  <div class="hero-photo abs" role="img" aria-label="Happy family with arms spread in a sunlit wheat field"></div>
  <svg class="abs" style="left:0;top:0" width="1200" height="1013" viewBox="0 0 1200 1013">
    <path d="M0 700 C 420 600 900 560 1200 110 L1200 1013 L0 1013 Z" fill="#f2f2f3"/>
    <path d="M0 700 C 120 655 230 630 330 615" stroke="#9b2a22" stroke-width="12" fill="none"/>
  </svg>
  <h1 class="hero-title abs">Vascular<br>Surgeon</h1>
  <div class="hero-sub abs">Vascular Surgeon in São Paulo</div>
  <div class="btn-pill btn-green abs" style="left:156px;top:390px;width:180px">
    <span class="ico"><svg width="14" height="14" viewBox="0 0 24 24" fill="none" stroke="#fff" stroke-width="2.4"><path d="M5 3h4l2 5-3 2a12 12 0 0 0 6 6l2-3 5 2v4a2 2 0 0 1-2 2A18 18 0 0 1 3 5a2 2 0 0 1 2-2z"/></svg></span>
    <span>Need help?<br>Chat via Chatline</span>
  </div>
  <div class="btn-pill btn-red abs" style="left:350px;top:390px;width:180px">
    <span class="ico"><svg width="14" height="14" viewBox="0 0 24 24" fill="none" stroke="#fff" stroke-width="2.4"><path d="M5 3h4l2 5-3 2a12 12 0 0 0 6 6l2-3 5 2v4a2 2 0 0 1-2 2A18 18 0 0 1 3 5a2 2 0 0 1 2-2z"/></svg></span>
    <span>Call Us Now!<br>(011) 4820-1170</span>
  </div>

  <form class="form-card abs">
    <h2>Schedule Now!</h2>
    <p>Please Complete the following in its entirety.</p>
    <div class="field abs" style="left:22px;top:120px;width:184px">NAME</div>
    <div class="field abs" style="left:220px;top:120px;width:184px">EMAIL</div>
    <div class="field abs" style="left:22px;top:172px;width:382px;height:112px">HOW CAN WE HELP ?</div>
    <div class="submit">SUBMIT</div>
  </form>

  <div class="hero-claim abs">Almost 40 years<br>taking care of you.<small>4 generations of doctors.</small></div>
</section>

<h2 class="section-title abs" style="top:1185px">Specialist in <span class="navy">Vascular Surgery</span><br>and <span class="red">Angiology</span></h2>

<div class="feature abs" style="top:1335px">
  <div class="icon"></div>
  <div><h3>Laser Treatment of Varicose Veins</h3><p>We do all venous treatments, from foam, laser, microsurgery, aesthetics and much more. Largest Brazilian experience in laser for varicose veins published.</p></div>
</div>
<div class="feature abs" style="top:1453px">
  <div class="icon"></div>
  <div><h3>Treatment of Lipedema</h3><p>We have a multiprofessional and multispecialized team in the treatment of lipedema.</p></div>
</div>
<div class="feature abs" style="top:1556px">
  <div class="icon"></div>
  <div><h3>All reimbursement agreements</h3><p>To make your life easier and guarantee the best treatment, we attend most of the agreements through free choice, that is, medical reimbursement</p></div>
</div>
<div class="img-fill abs" style="left:665px;top:1320px;width:372px;height:336px;background:linear-gradient(135deg,#d9b79c,#a8826a 55%,#6f6a5a)" role="img" aria-label="Woman's legs resting on a pebble beach"></div>

<section class="arterial abs">
  <div class="panel abs"></div>
  <div class="abs" style="left:132px;top:64px;width:429px;height:348px;background:radial-gradient(circle at 40% 40%,#e7b3b3,#c06a6a 60%,#9d3b3b)" role="img" aria-label="Red blood cells flowing in a vessel, video preview"></div>
  <div class="play abs" style="left:298px;top:186px"><span><svg width="18" height="20" viewBox="0 0 18 20"><path d="M3 1 L17 10 L3 19 Z" fill="#7d1f19"/></svg></span></div>
  <h2 class="abs display" style="left:650px;top:152px;font-size:40px;font-weight:600">Arterial diseases</h2>
  <p class="abs" style="left:650px;top:220px;width:440px;font-size:19px;line-height:33px;color:var(--text)">The vascular surgery team is used to endovascular and traditional arterial surgeries.</p>
</section>

<h2 class="section-title abs" style="top:2345px">Specialties</h2>
<svg class="abs" style="left:400px;top:2400px" width="400" height="360" viewBox="0 0 400 360">
  <circle cx="200" cy="180" r="150" fill="none" stroke="#d8d8dc" stroke-width="2"/>
  <circle cx="200" cy="180" r="92" fill="#e9e8ea"/>
</svg>
<div class="abs serif" style="left:500px;top:2565px;width:200px;text-align:center;font-size:22px;color:#333">Lumeria</div>
<div class="orbit-dot abs" style="left:471px;top:2428px"></div>
<div class="orbit-dot abs" style="left:642px;top:2425px"></div>
<div class="orbit-dot abs" style="left:408px;top:2557px"></div>
<div class="orbit-dot abs" style="left:708px;top:2557px"></div>
<div class="orbit-dot abs" style="left:471px;top:2685px"></div>
<div class="orbit-dot abs" style="left:642px;top:2685px"></div>
<div class="spec-label abs" style="left:258px;top:2444px">ARTERIAL SURGERY</div>
<div class="spec-label abs" style="left:746px;top:2441px">ENDOVASCULAR SURGERY</div>
<div class="spec-label abs" style="left:251px;top:2572px">VEIN SURGERY</div>
<div class="spec-label abs" style="left:802px;top:2562px;line-height:21px">VARICOSE VEIN<br>SURGERY LASER</div>
<div class="spec-label abs" style="left:222px;top:2708px">LYMPHATIC TREATMENT</div>
<div class="spec-label abs" style="left:746px;top:2708px">LIPOEDEMA</div>

<section class="testimonials abs">
  <h2 class="section-title abs" style="top:70px">Still having doubts?</h2>
  <p class="abs" style="width:1200px;top:118px;text-align:center;font-size:17px;color:#333">See the testimonies of our service. They had no doubts.</p>
  <div class="t-card abs" style="left:158px">
    <p>I had plastic surgery to treat Lipedema in early December 2019 and since the first contact I was very well attended.</p>
    <div class="t-person"><span class="avatar"></span><div><b>Helena</b><small>Northwind Studio</small></div><span class="quote">”</span></div>
  </div>
  <div class="t-card featured abs" style="left:460px">
    <p>I had plastic surgery to treat Lipedema in early December 2019 and since the first contact I was very well attended.</p>
    <div class="t-person"><span class="avatar"></span><div><b>Helena</b><small>Northwind Studio</small></div><span class="quote">”</span></div>
  </div>
  <div class="t-card abs" style="left:762px">
    <p>I had plastic surgery to treat Lipedema in early December 2019 and since the first contact I was very well attended.</p>
    <div class="t-person"><span class="avatar"></span><div><b>Helena</b><small>Northwind Studio</small></div><span class="quote">”</span></div>
  </div>
</section>

<section class="banner abs" role="img" aria-label="Family playing in a field at dusk">
  <h2>ANEURYSM SURGERY, CAROTID STENOSIS,<br>LASER VARICOSE VEINS AND OTHER VASCULAR DISEASES</h2>
  <div class="sub">Vascular Surgeon in São Paulo, SP</div>
  <div class="btn-pill btn-green abs" style="left:412px;top:208px;width:180px">
    <span class="ico"><svg width="14" height="14" viewBox="0 0 24 24" fill="none" stroke="#fff" stroke-width="2.4"><path d="M5 3h4l2 5-3 2a12 12 0 0 0 6 6l2-3 5 2v4a2 2 0 0 1-2 2A18 18 0 0 1 3 5a2 2 0 0 1 2-2z"/></svg></span>
    <span>Need help?<br>Chat via Chatline</span>
  </div>
  <div class="btn-pill btn-red abs" style="left:606px;top:208px;width:180px">
    <span class="ico"><svg width="14" height="14" viewBox="0 0 24 24" fill="none" stroke="#fff" stroke-width="2.4"><path d="M5 3h4l2 5-3 2a12 12 0 0 0 6 6l2-3 5 2v4a2 2 0 0 1-2 2A18 18 0 0 1 3 5a2 2 0 0 1 2-2z"/></svg></span>
    <span>Call Us Now!<br>(011) 4820-1170</span>
  </div>
  <svg class="abs" style="left:0;top:0" width="1200" height="490" viewBox="0 0 1200 490">
    <path d="M0 490 C 300 370 800 400 1200 150 L1200 490 Z" fill="#fff"/>
    <path d="M0 490 C 150 430 300 400 480 385" stroke="#9b2a22" stroke-width="12" fill="none"/>
  </svg>
</section>

<h2 class="section-title abs" style="top:3812px;left:-25px">Latest Blog</h2>

<article class="blog-card abs" style="left:132px">
  <div class="thumb" style="background:linear-gradient(180deg,#e8d2c5,#cfa997)" role="img" aria-label="Close-up of thighs showing cellulite"></div>
  <div class="body"><div class="date">February 1, 2021</div><h3>HOW IS THE TREATMENT OF LIPEDEMA?</h3><p>Lipedema is a chronic disease that targets women primarily. Rarely, lipedema affects men.</p><span class="more">LEARN MORE ›</span></div>
</article>
<article class="blog-card abs" style="left:463px">
  <div class="thumb" style="background:linear-gradient(180deg,#f1ede8,#d9c1b1)" role="img" aria-label="Row of women's legs against a light wall"></div>
  <div class="body"><div class="date">February 1, 2021</div><h3>LIPEDEMA: WHAT IS IT?</h3><p>Have you heard of lipedema? The disease, considered chronic by specialists, mainly affects women and its appearance has to</p><span class="more">LEARN MORE ›</span></div>
</article>
<article class="blog-card abs" style="left:793px">
  <div class="thumb" style="background:linear-gradient(135deg,#f3f1ee,#c9c4cf 50%,#c0404a)" role="img" aria-label="Yogurt jars with blueberries and raspberries"></div>
  <div class="body"><div class="date">February 1, 2021</div><h3>PROBIOTICS</h3><p>Probiotics are being used more and more in medicine. Probiotics are live bacteria, called "good bacteria" because they are</p><span class="more">LEARN MORE ›</span></div>
</article>
<div class="view-all abs">View All</div>

<footer class="site-footer abs">
  <p class="disclaimer abs">This site is oriented to the lay public. This website and its content are for informational purposes only and may not be suitable for all users. This website content does not replace the doctor. Everyone should always consult their doctor before making any decisions regarding their health. Book your appointment here. Dr Henrique Valença and Clinicor LTDA are not responsible for any content provided by non-affiliated third parties. See our privacy policy. Webmaster and Site Editor: Dr. Henrique Valença - CRM: 204.377</p>
  <div class="social abs"><span></span><span></span><span></span><span></span></div>

  <div class="f-head abs" style="left:613px;top:124px">CONTACT US</div>
  <div class="contact-row abs" style="left:617px;top:172px">
    <span class="c-ico"><svg width="12" height="14" viewBox="0 0 24 28" fill="#fff"><path d="M12 0a10 10 0 0 0-10 10c0 8 10 18 10 18s10-10 10-18A10 10 0 0 0 12 0zm0 14a4 4 0 1 1 0-8 4 4 0 0 1 0 8z"/></svg></span>Av. Aurora 1480, São Paulo, SP</div>
  <div class="contact-row abs" style="left:617px;top:224px">
    <span class="c-ico"><svg width="10" height="14" viewBox="0 0 10 16" fill="none" stroke="#fff" stroke-width="1.6"><rect x="1" y="1" width="8" height="14" rx="1.5"/></svg></span>(011) 4820-1170<br>Support 24/7 Weekdays</div>
  <div class="contact-row abs" style="left:617px;top:282px">
    <span class="c-ico"><svg width="14" height="10" viewBox="0 0 14 10" fill="none" stroke="#fff" stroke-width="1.4"><rect x="1" y="1" width="12" height="8"/><path d="M1 1l6 5 6-5"/></svg></span>consulta@lumeria.net</div>

  <div class="f-head abs" style="left:938px;top:124px">Info</div>
  <ul class="info-list abs" style="left:938px;top:168px">
    <li>Home</li><li>About Us</li><li>Vascular Problems</li><li>Solutions</li><li>Contact Us</li>
  </ul>

  <div class="copyright abs">© 2021 Lumeria. All Rights Reserved.</div>
  <div class="badge abs" style="left:732px;width:56px;height:56px;border-radius:50%;background:#c9a13b"></div>
  <div class="badge abs" style="left:806px;width:50px;height:58px;border-radius:6px 6px 25px 25px;background:#2d4f8f"></div>
  <div class="badge abs" style="left:880px;width:56px;height:56px;border-radius:50%;border:3px solid #e08a96"></div>
  <div class="badge abs" style="left:996px;top:382px;width:52px;height:26px;background:#d6d9e6"></div>
</footer>

</body>
</html>
```